Micro Markets Vending business needs a web design

I purchased a logo through MarkForge and asked them to design my website but was told they couldn't and that I needed to contact you.
I was building a website through Plyo using AI and liked what they had created verbiage-wise but I can't figure out how to finish it the way I would like it. Will send screen shots of what was written, and subsequently used in my slogan under my logo. Would like to use the colors in my logo for my website.
About the company:
TR Snackworks, LLC offers micro market vending machines. Swipe your card, open the doors, take what you want. Can be customized by size for the space, and items for sale within the machines. Pictures of the machines are attached as examples.
I don't need a Testimonials page right now since we are a new company, but will need to add one at some point.
I also like the idea of a contact us button, as shown in the last picture (although it says subscribe). We do not have any emails set up as of yet. Haven't figured out how to do that, but will.
Just let me know what files you need from MarkForge for my logo.
Target Market(s)
Apartment complexes, Buildings, Hotels, Gyms, etc
Industry/Entity Type
Vending Machines
Coding
Coded - Design and coding required
Number of Pages Required
1 page
Font styles to use
Other font styles liked:
- Your choice on font style that complements our logo font.
Look and feel
Each slider illustrates characteristics of the customer's brand and the style your logo design should communicate.

```html
<!DOCTYPE html>
<html lang="en">
<head>
<meta charset="utf-8">
<title>TR Snackworks, LLC</title>
<link rel="stylesheet" href="https://fonts.googleapis.com/css2?family=Lexend:wght@300;400;500&family=Righteous&display=swap">
<style>
:root{
  --green:#5cff0a;
  --dark:#0c0e0e;
  --ink:#1d1d1d;
  --white:#ffffff;
}
*{box-sizing:border-box;margin:0;padding:0}
html,body{width:1200px;height:2321px;overflow:hidden}
body{position:relative;font-family:"Lexend",sans-serif;color:var(--ink);background:var(--white)}
.abs{position:absolute}
.outline-title{font-family:"Righteous",sans-serif;color:var(--white);-webkit-text-stroke:1.6px #2a2a2a;text-shadow:2px 2px 0 #bdbdbd;letter-spacing:.5px;font-weight:400}
.btn{display:inline-flex;align-items:center;justify-content:center;background:var(--green);color:#111;border-radius:22px;font-size:14px;font-weight:400;text-transform:uppercase;text-decoration:none}

/* hero */
.hero{left:0;top:0;width:1200px;height:640px;background:linear-gradient(135deg,#f4f4f4 0%,#e6e6e6 60%,#d6d6d6 100%)}
.brand{left:112px;top:108px;display:flex;align-items:center;gap:10px;font-family:"Righteous",sans-serif;font-size:25px;color:#222}
.brand-mark{width:22px;height:22px;background:var(--green);border-radius:4px;flex:none}
.nav{left:586px;top:40px;display:flex;font-size:14.5px;text-transform:uppercase}
.nav a{color:#222;text-decoration:none;padding:7px 7px;border-radius:18px;margin-right:26px}
.nav a.active{background:var(--green);margin-right:22px}
.hero-title{left:110px;top:192px;font-size:35px}
.hero-text{left:114px;top:255px;width:520px;font-size:15.5px;line-height:35px;font-weight:300;color:#222}
.hero-btn{left:112px;top:418px;width:136px;height:40px}
.machine-photo{left:722px;top:77px;width:252px;height:458px;background:linear-gradient(180deg,#5a5d60 0%,#3a3c3e 60%,#2a2b2c 100%);border-radius:3px}
.swoosh{left:0;top:340px}

/* about */
.about{left:0;top:620px;width:1200px;height:528px;background:radial-gradient(ellipse at 70% 30%,#1d2122 0%,var(--dark) 75%)}
.about-frame{left:110px;top:647px;width:460px;height:430px;border:2px solid var(--green);border-radius:22px}
.about-photo{left:118px;top:647px;width:453px;height:422px;border-radius:22px;background:linear-gradient(160deg,#7a4a38 0%,#2e2a2c 45%,#1a1c22 100%)}
.about-title{left:634px;top:648px;font-size:29px;color:var(--white);font-weight:400}
.about-title span{color:var(--green)}
.about-text{left:634px;top:705px;width:465px;font-size:15.5px;line-height:35px;font-weight:300;color:#d9d9d9}
.about-text p+p{margin-top:14px}
.about-btn{left:633px;top:1029px;width:152px;height:39px}

/* why choose us */
.why-title{left:0;top:1222px;width:1200px;text-align:center;font-size:35px}
.why-text{left:190px;top:1287px;width:820px;text-align:center;font-size:15px;line-height:34px;font-weight:300;color:#333}
.card{top:1396px;width:315px;height:400px}
.card-body{position:absolute;left:0;top:0;width:315px;height:400px;background:var(--white);border-radius:22px;box-shadow:0 6px 22px rgba(0,0,0,.08);overflow:hidden;text-align:center}
.card-corner{position:absolute;left:0;top:0}
.card-icon{position:absolute;left:18px;top:12px}
.card-title{position:absolute;left:0;top:72px;width:100%;font-size:20.5px;font-weight:400;text-transform:uppercase;color:#49e000}
.card-sub{position:absolute;left:0;top:118px;width:100%;font-size:16.5px;font-weight:400;color:#555;text-transform:uppercase}
.card-text{position:absolute;left:26px;top:152px;width:263px;font-size:15px;line-height:31px;font-weight:300;color:#6a6a6a}
.card-bar{position:absolute;left:0;top:366px;width:315px;height:34px;background:var(--green)}
.card-tip{position:absolute;left:143px;top:399px;width:0;height:0;border-left:14px solid transparent;border-right:14px solid transparent;border-top:16px solid var(--green)}
.card-num{top:1830px;width:315px;text-align:center;font-size:34px}

/* newsletter */
.newsletter{left:0;top:1948px;width:1200px;height:86px;background:var(--green)}
.news-title{left:112px;top:1975px;font-size:24px;-webkit-text-stroke:1.2px #1a1a1a;text-shadow:2px 2px 0 #2d8d00}
.news-field{left:628px;top:1973px;width:460px;height:38px;border-radius:20px;background:linear-gradient(90deg,rgba(78,230,4,0),#4ee604);padding-left:24px;display:flex;align-items:center;font-size:13px;color:#1a1a1a}
.news-btn{left:937px;top:1973px;width:151px;height:38px;border-radius:20px;background:#111;color:var(--green);display:flex;align-items:center;justify-content:center;font-size:14px}

/* footer */
.footer{left:0;top:2034px;width:1200px;height:287px;background:var(--dark)}
.foot-brand{left:90px;top:2180px;width:266px;display:flex;align-items:center;justify-content:center;gap:10px;font-family:"Righteous",sans-serif;font-size:22px;color:var(--white)}
.foot-links{top:2092px;list-style:none;font-size:14.5px;text-transform:uppercase;color:var(--white)}
.foot-links li{height:38px}
.foot-contact{left:880px;display:flex;gap:24px;font-size:14.5px;color:var(--white);text-transform:uppercase;line-height:30px}
.foot-icon{width:35px;height:35px;border-radius:50%;background:#2a2d2e;display:flex;align-items:center;justify-content:center;flex:none}
.foot-rule{left:72px;top:2265px;width:1056px;height:1px;background:#2b2e2f}
.copyright{left:0;top:2288px;width:1200px;text-align:center;font-size:12.5px;color:var(--white);text-transform:uppercase}
.copyright span{color:var(--green)}
</style>
</head>
<body>

<section class="hero abs"></section>
<div class="machine-photo abs" role="img" aria-label="Photo of a dark glass-front snack vending machine against a white brick wall"></div>

<svg class="swoosh abs" width="1200" height="290" viewBox="0 340 1200 290" aria-hidden="true">
  <path d="M0 620 C90 560 220 505 330 505 C500 500 650 575 850 572 C1000 565 1120 480 1200 430 V630 H0 Z" fill="var(--dark)"/>
  <path d="M0 548 C90 520 220 505 330 505 C200 512 80 560 0 620 Z" fill="var(--green)"/>
  <path d="M1200 350 V430 C1110 520 990 568 850 572 C1000 555 1120 470 1200 350 Z" fill="var(--green)"/>
</svg>

<section class="about abs"></section>

<div class="brand abs"><span class="brand-mark"></span>TR Snackworks, LLC</div>

<nav class="nav abs">
  <a class="active" href="#">Home</a>
  <a href="#">About Us</a>
  <a href="#">Why Choose Us</a>
  <a href="#">Contact Us</a>
</nav>

<h1 class="hero-title outline-title abs">DISCOVER OUR RANGE</h1>
<p class="hero-text abs">Welcome to TR Snackworks, where convenience meets customization. Our micro market vending machines in Greater Houston, TX, offer a variety of snacks and drinks tailored to your preferences. Swipe your credit card, open the doors, and indulge in what you desire.</p>
<a class="hero-btn btn abs" href="#">Contact Us</a>

<div class="about-frame abs"></div>
<div class="about-photo abs" role="img" aria-label="Photo of a two-door micro market fridge stocked with snacks and drinks in front of a brick wall"></div>
<h2 class="about-title abs">ABOUT <span>TR SNACKWORKS, LLC</span></h2>
<div class="about-text abs">
  <p>At TR Snackworks, we are dedicated to revolutionizing the vending experience. Our mission is to provide a convenient way for you to access your favorite snacks and drinks in a hassle-free manner.</p>
  <p>With a focus on customer satisfaction, we ensure that our products are always fresh and our machines are well maintained. Experience the future of vending with TR Snackworks, LLC.</p>
</div>
<a class="about-btn btn abs" href="#">Explore More</a>

<h2 class="why-title outline-title abs">WHY CHOOSE US</h2>
<p class="why-text abs">TR Snackworks stands out for its commitment to quality, convenience, and customization. We prioritize customer preferences and aim to provide a seamless vending experience.</p>

<div class="card abs" style="left:111px">
  <div class="card-body">
    <svg class="card-corner" width="88" height="78" viewBox="0 0 88 78" aria-hidden="true"><path d="M0 0 H86 C70 40 40 70 0 78 Z" fill="var(--green)"/></svg>
    <svg class="card-icon" width="34" height="34" viewBox="0 0 34 34" aria-hidden="true" fill="none" stroke="#111" stroke-width="1.8"><path d="M5 13 L17 7 L29 13 L17 19 Z M5 13 V25 L17 31 L29 25 V13 M17 19 V31"/><path d="M12 5 L15 8 L21 2"/></svg>
    <h3 class="card-title">Quality Products</h3>
    <p class="card-sub">Fresh and Varied Selection</p>
    <p class="card-text">Our vending machines are stocked with a diverse range of snacks and drinks, ensuring that there's something for everyone. We source only the freshest products for your enjoyment.</p>
    <div class="card-bar"></div>
  </div>
  <div class="card-tip"></div>
</div>
<div class="card abs" style="left:442px">
  <div class="card-body">
    <svg class="card-corner" width="88" height="78" viewBox="0 0 88 78" aria-hidden="true"><path d="M0 0 H86 C70 40 40 70 0 78 Z" fill="var(--green)"/></svg>
    <svg class="card-icon" width="34" height="34" viewBox="0 0 34 34" aria-hidden="true" fill="none" stroke="#111" stroke-width="1.8"><rect x="8" y="4" width="16" height="26" rx="2"/><path d="M12 10 H20 M12 16 H20 M12 22 H16"/></svg>
    <h3 class="card-title">Convenience</h3>
    <p class="card-sub">Easy Access Anytime</p>
    <p class="card-text">With TR Snackworks, snack time is just a swipe away. Our machines are strategically located for your convenience, providing quick and easy access to your favorite treats.</p>
    <div class="card-bar"></div>
  </div>
  <div class="card-tip"></div>
</div>
<div class="card abs" style="left:773px">
  <div class="card-body">
    <svg class="card-corner" width="88" height="78" viewBox="0 0 88 78" aria-hidden="true"><path d="M0 0 H86 C70 40 40 70 0 78 Z" fill="var(--green)"/></svg>
    <svg class="card-icon" width="34" height="34" viewBox="0 0 34 34" aria-hidden="true" fill="none" stroke="#111" stroke-width="1.8"><circle cx="17" cy="17" r="10"/><circle cx="17" cy="17" r="4"/><path d="M17 3 V7 M17 27 V31 M3 17 H7 M27 17 H31"/></svg>
    <h3 class="card-title">Customization</h3>
    <p class="card-sub">Tailored to Your Tastes</p>
    <p class="card-text">Personalize your snacking experience with TR Snackworks. Choose from a wide selection of snacks and drinks to create a vending experience that suits your unique preferences.</p>
    <div class="card-bar"></div>
  </div>
  <div class="card-tip"></div>
</div>
<div class="card-num outline-title abs" style="left:111px">01</div>
<div class="card-num outline-title abs" style="left:442px">02</div>
<div class="card-num outline-title abs" style="left:773px">03</div>

<section class="newsletter abs"></section>
<h2 class="news-title outline-title abs">STAY UPDATED WITH TR SNACKWORKS</h2>
<div class="news-field abs">EMAIL ADDRESS</div>
<div class="news-btn abs">SUBSCRIBE NOW</div>

<footer class="footer abs"></footer>
<div class="foot-brand abs"><span class="brand-mark"></span>TR SNACKWORKS, LLC</div>
<ul class="foot-links abs" style="left:446px"><li>Home</li><li>About Us</li><li>Why Choose Us</li><li>Contact Us</li></ul>
<ul class="foot-links abs" style="left:672px"><li>Terms of Use</li><li>Privacy Policy</li><li>Site Map</li><li>Cookies</li></ul>
<div class="foot-contact abs" style="top:2086px">
  <span class="foot-icon"><svg width="14" height="14" viewBox="0 0 24 24" aria-hidden="true"><path fill="#fff" d="M6.6 10.8a15 15 0 0 0 6.6 6.6l2.2-2.2c.3-.3.7-.4 1-.2 1.1.4 2.3.6 3.6.6.6 0 1 .4 1 1V20c0 .6-.4 1-1 1A17 17 0 0 1 3 4c0-.6.4-1 1-1h3.5c.6 0 1 .4 1 1 0 1.3.2 2.5.6 3.6.1.3 0 .7-.2 1z"/></svg></span>
  <span style="padding-top:3px">+1 555 014 2290</span>
</div>
<div class="foot-contact abs" style="top:2142px">
  <span class="foot-icon"><svg width="14" height="16" viewBox="0 0 24 28" aria-hidden="true"><path fill="#fff" d="M12 0C6.5 0 2 4.3 2 9.7 2 17 12 28 12 28s10-11 10-18.3C22 4.3 17.5 0 12 0zm0 13.5a4 4 0 1 1 0-8 4 4 0 0 1 0 8z"/></svg></span>
  <span style="padding-top:3px">52, TR Snackworks Lorem<br>Sit Amet 604 217</span>
</div>
<div class="foot-rule abs"></div>
<p class="copyright abs">@2024 Copyrights - <span>TR Snackworks LLC</span> - All Rights Reserved</p>

</body>
</html>
```